Firma für Arbeitssicherheit sucht Flyer-Design
Zielgruppe
Wir sind eine Firma für Arbeitssicherheit.
Für unsere Notleuchten Abteilung benötigen wir einen ganz neuen Flyer.
Zur Ansicht setllen wir den alten Flyer zur Verfügung. Bilder, Tabellen und Texte können dann gesendet werden.
Die Zielgruppe sind Elektriker.
Aufgabenstellung
die dazugehörige Internetseite ist: www.quorvex-licht.example
Der Flyer soll ansprechender, peppiger, moderner, chicer sein, als der alte Flyer.

```html
<!DOCTYPE html>
<html lang="de">
<head>
<meta charset="utf-8">
<title>Quorvex – LED-Lichtlösungen Flyer</title>
<link rel="stylesheet" href="https://fonts.googleapis.com/css2?family=Arimo:wght@400;700&display=swap">
<style>
:root{
  --orange:#f3a42a;
  --orange-deep:#ee9a1c;
  --ink:#222;
  --muted:#555;
  --line:#d9d9d9;
  --row:#f1f1f1;
  --paper:#fff;
}
*{margin:0;padding:0;box-sizing:border-box}
html,body{width:1200px;height:900px;overflow:hidden;background:var(--paper);font-family:"Arimo",Arial,sans-serif;color:var(--ink)}
.canvas{position:relative;width:1200px;height:900px}

/* cover */
.cover{position:absolute;left:392px;top:22px;width:396px;height:398px;overflow:hidden}
.cover-photo{position:absolute;inset:0;background:radial-gradient(circle at 44% 45%,#fff6df 0,#f5d9a8 14%,#b9a594 32%,#8f8886 55%,#6f6c6d 100%)}
.cover-brand{position:absolute;right:30px;top:16px;text-align:right;color:var(--orange)}
.cover-brand .name{font-size:34px;font-weight:700;letter-spacing:1px;line-height:1}
.cover-brand .tag{font-size:6.5px;letter-spacing:1.2px;color:#f7c57a;margin-top:3px}
.cover-banner{position:absolute;left:62px;right:0;top:74px;height:36px;background:var(--orange);color:#fff;font-weight:700;font-size:11.5px;line-height:14px;text-align:center;padding-top:4px}
.cover-mark{position:absolute;left:182px;top:363px;font-size:5.5px;color:#fff;display:flex;align-items:center;gap:6px}
.cover-mark .badge{width:54px;height:19px;background:#fff;border:2px solid #4a9b3a}

/* inner pages */
.page{position:absolute;top:480px;width:366px;height:398px;border:1px solid #ccc;background:var(--paper)}
.page-left{left:168px}
.page-right{left:632px}
.page-tab{position:absolute;top:-1px;width:26px;height:132px;background:var(--orange);display:flex;align-items:center;justify-content:center}
.page-tab span{writing-mode:vertical-rl;transform:rotate(180deg);color:#fff;font-weight:700;font-size:10px;letter-spacing:.5px;white-space:nowrap}
.page-left .page-tab{left:-1px}
.page-right .page-tab{right:-1px}
.page-num{position:absolute;bottom:-1px;width:26px;height:31px;background:var(--orange);color:#fff;font-size:7px;font-weight:700;display:flex;align-items:center;justify-content:center}
.page-left .page-num{left:-1px}
.page-right .page-num{right:-1px}
.page-title{position:absolute;top:34px;color:var(--orange);font-size:20px;font-weight:700}
.page-subtitle{position:absolute;font-size:7.5px;font-weight:700}
.page-left .page-title,.page-left .page-subtitle{left:45px}
.page-right .page-title,.page-right .page-subtitle{left:35px}
.page-url{position:absolute;bottom:14px;font-size:5.5px;color:var(--muted)}
.page-left .page-url{right:28px}
.page-right .page-url{left:35px}

.features{position:absolute;width:150px;font-size:4.6px;line-height:6px}
.features h4{font-size:5px;margin-bottom:5px}
.features li{list-style:none;position:relative;padding-left:6px;margin-bottom:4.5px}
.features li::before{content:"";position:absolute;left:0;top:1px;width:3.5px;height:3.5px;background:var(--orange)}

.product-shot{position:absolute}
.lamp-round{left:214px;top:94px;width:112px;height:82px;background:radial-gradient(ellipse at 50% 35%,#ffffff 0,#f3f3f3 45%,#cfcfcf 80%,#fff 100%);border-radius:50% 50% 46% 46%/60% 60% 40% 40%}
.lamp-tube{left:190px;top:150px;width:178px;height:32px;border-radius:16px;background:linear-gradient(180deg,#eef2f6,#c7ced6 55%,#9aa3ad);transform:rotate(-28deg)}

.certs{position:absolute;display:flex;gap:3px}
.certs i{display:block;width:11px;height:9px;border:1px solid #bbb}
.certs i.hi{background:#f6e27a;border-color:#e7c93a}
.warranty{position:absolute;font-size:7px;font-weight:700;color:#666;display:flex;align-items:center;gap:3px}

.spec-table{position:absolute;left:50px;top:260px;width:286px;border-collapse:collapse;font-size:4.6px}
.spec-table .band th{background:var(--orange);color:#fff;height:19px;text-align:left;padding-left:6px}
.spec-table .band th:first-child{font-size:9px}
.spec-table .band th:last-child{font-size:4.6px;line-height:6px}
.spec-table .heads th{font-weight:400;height:13px;border-bottom:1px solid var(--line)}
.spec-table td{height:13px;text-align:center;border-bottom:1px solid #fff}
.spec-table tbody tr:nth-child(odd) td{background:var(--row)}
</style>
</head>
<body>
<div class="canvas">

  <section class="cover">
    <div class="cover-photo" role="img" aria-label="Foto einer leuchtenden Glühlampe in einem Drahtkorb vor grauer Decke"></div>
    <div class="cover-brand">
      <div class="name">quorvex</div>
      <div class="tag">PROFESSIONAL LIGHTING SOLUTIONS</div>
    </div>
    <div class="cover-banner">Professionelle LED-Lichtlösungen &amp; Notleuchten<br>für Büro, Verwaltung und Industrie</div>
    <div class="cover-mark">eine Marke von <span class="badge"></span></div>
  </section>

  <section class="page page-left">
    <div class="page-tab"><span>LED - LEUCHTEN</span></div>
    <h2 class="page-title">RUNDA-LED</h2>
    <p class="page-subtitle" style="top:66px">RUNDA-LED – Die LED-Wannenleuchte für Büro, Verwaltung &amp; Wohngebäude</p>
    <div class="features" style="left:45px;top:92px">
      <h4>Produktmerkmale</h4>
      <ul>
        <li>energiesparend und wartungsarm, eine ansprechende und installationsfreundliche Lösung</li>
        <li>optimale Lichtqualität und reduzierte Blendung durch moderne LED-Technologie</li>
        <li>die ideale Lösung für Anwendungen in Treppenhäusern und Fluren</li>
        <li>opale, stoßfeste Abdeckung (PMMA)</li>
        <li>geprüfte LED-Lebensdauer von mindestens 50.000 Stunden</li>
        <li>für Wand- und Deckenmontage geeignet</li>
        <li>umweltfreundlich, inklusive RoHS-Zertifikat</li>
        <li>CE-Zeichen</li>
      </ul>
    </div>
    <div class="product-shot lamp-round" role="img" aria-label="Produktfoto der runden LED-Deckenleuchte mit opaler Abdeckung"></div>
    <div class="certs" style="left:200px;top:200px"><i></i><i></i><i></i><i></i><i></i><i class="hi"></i></div>
    <div class="warranty" style="left:200px;top:214px">★ 5 JAHRE GARANTIE</div>
    <table class="spec-table">
      <thead>
        <tr class="band"><th colspan="2">RUNDA-LED</th><th colspan="5">LED-Rundleuchte mit einer opalen PMMA-Abdeckung<br>Wand-/Deckenmontage, 230V ~ 50Hz, Schutzart IP 44</th></tr>
        <tr class="heads"><th>Artikel-Nr.</th><th>Leistung</th><th>Leuchtmittel</th><th>Farbtemperatur</th><th>Lichtstrom</th><th>Durchmesser</th><th>Aktionspreis</th></tr>
      </thead>
      <tbody>
        <tr><td>QV RL 012</td><td>12 W</td><td>LED</td><td>4000 K</td><td>1020 lm</td><td>250 mm</td><td>19,50 €</td></tr>
        <tr><td>QV RL 012</td><td>12 W</td><td>LED</td><td>4000 K</td><td>1020 lm</td><td>250 mm</td><td>19,50 €</td></tr>
        <tr><td>QV RL 012</td><td>12 W</td><td>LED</td><td>4000 K</td><td>1020 lm</td><td>250 mm</td><td>19,50 €</td></tr>
        <tr><td>QV RL 012</td><td>12 W</td><td>LED</td><td>4000 K</td><td>1020 lm</td><td>250 mm</td><td>19,50 €</td></tr>
        <tr><td>QV RL 012</td><td>3 h / 8 h &nbsp;12 W</td><td>LED</td><td>4000 K</td><td>1020 lm</td><td>250 mm</td><td>19,50 €</td></tr>
      </tbody>
    </table>
    <p class="page-url">www.quorvex-licht.example</p>
    <div class="page-num">2</div>
  </section>

  <section class="page page-right">
    <div class="page-tab"><span>LED - LEUCHTEN</span></div>
    <h2 class="page-title">LINEA-LED STANDARD No. 2</h2>
    <p class="page-subtitle" style="top:76px">Die LED-Feuchtraum-Wannenleuchte für die Industrie</p>
    <div class="features" style="left:35px;top:98px">
      <h4>Produktmerkmale</h4>
      <ul>
        <li>energiesparend und wartungsarm, eine ansprechende und installationsfreundliche Lösung</li>
        <li>optimale Lichtqualität und reduzierte Blendung durch moderne LED-Technologie</li>
        <li>4 Ausführungen für den herkömmlichen Ersatz von 1x18 W, 1x36 W, 1x58 W</li>
        <li>die ideale Lösung für Anwendungen in Parkhäusern, Lagerhallen und Industrieanlagen</li>
        <li>robustes, schlagfestes (PC), spritzwasser- und staubdichtes Gehäuse (IP65)</li>
        <li>werkzeuglose Montage der Leuchte durch Abziehen der Abdeckung</li>
        <li>geprüfte LED-Lebensdauer von mindestens 50.000 Stunden</li>
        <li>für Wand- und Deckenmontage geeignet, inklusive Befestigungsmaterial</li>
        <li>umweltfreundlich, inklusive RoHS-Zertifikat</li>
        <li>mit CE-Zulassung, CE-Zeichen</li>
      </ul>
      <h4 style="margin-top:10px">Material</h4>
      <ul>
        <li>Gehäuse: Polycarbonat, robust, schlagfest</li>
        <li>Farbe: RAL 7035 (grau)</li>
        <li>Abdeckung: Polycarbonat, opal, robust, schlagfest</li>
      </ul>
    </div>
    <div class="product-shot lamp-tube" role="img" aria-label="Produktfoto der länglichen LED-Feuchtraum-Wannenleuchte"></div>
    <div class="certs" style="left:226px;top:236px"><i></i><i></i><i></i><i></i><i></i><i class="hi"></i></div>
    <div class="warranty" style="left:226px;top:250px">★ 5 JAHRE GARANTIE</div>
    <p class="page-url">www.quorvex-licht.example</p>
    <div class="page-num">3</div>
  </section>

</div>
</body>
</html>
```